The Open Compass Field Journeys Travel Brochure

I'm looking for a brochure design for a new travel product - The Open Compass Field Journeys, catering for students above 12 years old. Target audience are schools that do destination projects. Brochure to be read by head teacher, parents and students.

Brochure should be A4 in size, 4-6 pages. Format of brochure is hard cover (a folder) with inlet for flyers. Flyers for destinations will be updated from time to time.

Finished job needs to be converted to electronic format for website and email proposal usage.

Attached is text to be used on brochure. Order of section can be adjusted.

For "Elements of the trip", please understand the contents and explain/display it in a graphic form.

For flyer, please come out with a template that I can use for other destinations. The main elements - what's included, number of days, location for pictures, itinerary, educational focus, should be alterable. Attached are text for two sample destinations.
Also attached (tour itinerary example) a version of flyer that I like.

I'm attaching some pictures here. If you find more suitable pictures, please feel free to use them.

Reason: I'm extending the deadline of this project by 4 days, as I need to add details & photo of another travel specialist in personnel session (total of 3 members). Also, in view of the amount of work a designer has to do for this project, I'm giving you more time for submission. Please do not hesitate to be in touch should you need more than 4 days extension. Thank you.

Target Market(s)

Schools - especially the head teacher and parents, to send students above 12 years old to travel

Industry/Entity Type

Electronic

Requirements
Must have
• This is a travel brochure with education elements in it. Parents feel better when their children are travelling for a purpose and lead by responsible teachers/adults whom they can trust. So, the design has to emphasis that education elements and safety are our utmost priority.
Nice to have
• We specialise in environmental study. So, it is nice to have the environmental touch in the design.
Should not have
• Our target market segment is the Middle East, which can be quite sensitive to religion. I prefer not to have any religious related illustration on the design.

```html
<!DOCTYPE html>
<html lang="en">
<head>
<meta charset="utf-8">
<title>The Open Compass Field Journeys – Brochure Cover</title>
<link rel="stylesheet" href="https://fonts.googleapis.com/css2?family=Righteous&display=swap">
<style>
  :root {
    --sky-haze: #c9d3e2;
    --ridge-blue: #7f93b4;
    --valley-tan: #a98a6c;
    --slope-amber: #c07a2c;
    --slope-rust: #8a4a1c;
    --shadow-earth: #3d2616;
    --veil: rgba(250, 248, 245, 0.78);
    --divider: #ffffff;
    --ink-dark: #2b1a10;
    --ink-mid: #6b3f22;
    --ink-light: #b88658;
  }
  * { margin: 0; padding: 0; box-sizing: border-box; }
  html, body {
    width: 848px;
    height: 1200px;
    overflow: hidden;
    background: #ffffff;
  }
  .cover {
    position: relative;
    width: 848px;
    height: 1200px;
    overflow: hidden;
  }
  .cover-art {
    position: absolute;
    inset: 0;
    width: 848px;
    height: 1200px;
  }
  .plane-icon {
    position: absolute;
    left: 703px;
    top: 443px;
    width: 82px;
    height: 82px;
  }
  .cover-title {
    position: absolute;
    right: 48px;
    top: 570px;
    text-align: right;
    font-family: "Righteous", "Arial Black", sans-serif;
    font-weight: 400;
    font-size: 72px;
    line-height: 106px;
    letter-spacing: 4px;
    text-transform: uppercase;
    background: linear-gradient(100deg, var(--ink-dark) 0%, var(--ink-mid) 45%, var(--ink-light) 100%);
    -webkit-background-clip: text;
    background-clip: text;
    color: transparent;
  }
  .cover-title .line {
    display: block;
    white-space: nowrap;
  }
  .globe-letter {
    display: inline-block;
    width: 62px;
    height: 62px;
    vertical-align: -4px;
    margin-right: 2px;
  }
  .pointer-globe {
    display: inline-block;
    vertical-align: -12px;
    margin-right: 18px;
  }
</style>
</head>
<body>
<main class="cover">
  <svg class="cover-art" viewBox="0 0 848 1200" role="img"
       aria-label="Photograph of an ancient stone wall winding along autumn mountain ridges under hazy blue peaks, split diagonally with a faded wash on the right">
    <defs>
      <linearGradient id="landscape" x1="0" y1="0" x2="0.3" y2="1">
        <stop offset="0" stop-color="var(--sky-haze)"/>
        <stop offset="0.12" stop-color="var(--ridge-blue)"/>
        <stop offset="0.28" stop-color="var(--valley-tan)"/>
        <stop offset="0.45" stop-color="var(--slope-amber)"/>
        <stop offset="0.7" stop-color="var(--slope-rust)"/>
        <stop offset="1" stop-color="var(--shadow-earth)"/>
      </linearGradient>
    </defs>
    <rect class="photo-fill" width="848" height="1200" fill="url(#landscape)"/>
    <polygon class="faded-panel" points="848,92 848,1200 68,1200" fill="var(--veil)"/>
    <polygon class="diagonal-divider" points="836,22 848,22 848,40 22,1200 6,1200" fill="var(--divider)"/>
  </svg>

  <svg class="plane-icon" viewBox="0 0 24 24" aria-hidden="true">
    <path fill="var(--ink-mid)" transform="rotate(45 12 12)"
          d="M21 16v-2l-8-5V3.5a1.5 1.5 0 0 0-3 0V9l-8 5v2l8-2.5V19l-2 1.5V22l3.5-1 3.5 1v-1.5L13 19v-5.5z"/>
  </svg>

  <h1 class="cover-title">
    <span class="line">The</span>
    <span class="line"><svg class="globe-letter" viewBox="0 0 64 64" aria-hidden="true"><circle cx="32" cy="32" r="30" fill="var(--ink-dark)"/><g fill="none" stroke="#e8ddd2" stroke-width="2"><circle cx="32" cy="32" r="14"/><ellipse cx="32" cy="32" rx="6" ry="14"/><line x1="18" y1="32" x2="46" y2="32"/><line x1="20" y1="25" x2="44" y2="25"/><line x1="20" y1="39" x2="44" y2="39"/></g></svg>pen</span>
    <span class="line">Compass</span>
    <span class="line"><svg class="pointer-globe" width="170" height="80" viewBox="0 0 170 80" aria-hidden="true"><g fill="var(--ink-dark)"><rect x="0" y="34" width="64" height="10" rx="3"/><polygon points="60,26 78,39 60,52"/></g><g fill="none" stroke="var(--ink-dark)" stroke-width="5"><circle cx="126" cy="40" r="35"/><ellipse cx="126" cy="40" rx="15" ry="35"/><line x1="91" y1="40" x2="161" y2="40"/><line x1="96" y1="22" x2="156" y2="22"/><line x1="96" y1="58" x2="156" y2="58"/></g></svg>Field</span>
    <span class="line">Journeys</span>
  </h1>
</main>
</body>
</html>
```